Healthcare IT company looking for business card design

We develop IT systems for healthcare that significantly reduces cost and improves quality.

We want a business card design that is professional and clean, and using the colors in our logo.

Target Market(s)

Doctors and decision makers in the healthcare industry

Industry/Entity Type

Healthcare

Contact Information for Business Card

It should include
Name and title, address, telephone

Tobias Vrenholt, CEO
+46 712 418257
tobias@kelvaro.se

Font styles to use
Serif

Colors
0355a3
ed282f

Requirements
Must have
• Clean design
• Professional feel
Nice to have
• N/A
Should not have
• N/A

```html
<!DOCTYPE html>
<html lang="en">
<head>
<meta charset="utf-8">
<title>Kelvaro business card</title>
<link rel="stylesheet" href="https://fonts.googleapis.com/css2?family=EB+Garamond:wght@400;600&display=swap">
<style>
  :root {
    --brand-blue: #0355a3;
    --brand-blue-deep: #0b4a8f;
    --brand-red: #ed282f;
    --paper: #f7f7f7;
    --backdrop: #2a2a2a;
    --ink-light: #e6ecf4;
    --ink-muted: #9fb4cf;
  }
  * { box-sizing: border-box; margin: 0; padding: 0; }
  html, body {
    width: 1200px; height: 873px; overflow: hidden;
    background: var(--backdrop);
    font-family: "EB Garamond", Georgia, serif;
  }
  .stage { position: relative; width: 1200px; height: 873px; }
  .card {
    position: absolute; width: 520px; height: 298px;
    background: var(--paper); overflow: hidden;
    box-shadow: 0 12px 30px rgba(0,0,0,.55);
  }
  .card--front { left: 80px; top: 110px; }
  .card--back { left: 600px; top: 460px; }
  .card__wave { position: absolute; inset: 0; width: 100%; height: 100%; }
  .wordmark {
    position: absolute; font-weight: 600; color: var(--brand-blue);
    letter-spacing: 1px; display: flex; align-items: center; gap: 10px;
  }
  .wordmark__dot {
    width: 14px; height: 14px; border-radius: 50%; background: var(--brand-red);
  }
  .card--front .wordmark { left: 100px; top: 78px; font-size: 74px; }
  .card--back .wordmark { left: 150px; top: 36px; font-size: 58px; }
  .website {
    position: absolute; left: 268px; top: 246px;
    font-size: 14px; letter-spacing: 3px; color: var(--ink-muted);
    transform: rotate(-22deg); transform-origin: left center;
  }
  .holder {
    position: absolute; left: 120px; top: 218px; text-align: right; width: 200px;
  }
  .holder__name { font-size: 20px; font-weight: 600; color: var(--ink-light); }
  .holder__title { font-size: 12px; color: var(--ink-muted); letter-spacing: 1px; }
  .divider {
    position: absolute; left: 345px; top: 170px; width: 1px; height: 100px;
    background: linear-gradient(transparent, rgba(255,255,255,.7), transparent);
  }
  .contacts { position: absolute; left: 362px; top: 176px; list-style: none; }
  .contacts li {
    display: flex; align-items: center; gap: 8px;
    font-size: 14px; color: var(--ink-light); height: 27px;
  }
  .contacts svg { width: 16px; height: 16px; fill: var(--ink-light); flex: none; }
</style>
</head>
<body>
<main class="stage">
  <section class="card card--front" aria-label="Card front">
    <svg class="card__wave" viewBox="0 0 520 298" preserveAspectRatio="none" aria-hidden="true">
      <path d="M0 298 C 160 200 330 150 520 128 L520 298 Z" fill="var(--brand-red)"/>
      <path d="M0 298 C 160 206 330 156 520 135 L520 298 Z" fill="var(--brand-blue)"/>
    </svg>
    <div class="wordmark">Kelvaro<span class="wordmark__dot"></span></div>
    <p class="website">www.kelvaro.se</p>
  </section>

  <section class="card card--back" aria-label="Card back">
    <svg class="card__wave" viewBox="0 0 520 298" preserveAspectRatio="none" aria-hidden="true">
      <path d="M0 200 C 150 140 330 125 520 118 L520 298 L0 298 Z" fill="var(--brand-red)"/>
      <path d="M0 206 C 150 147 330 132 520 125 L520 298 L0 298 Z" fill="var(--brand-blue)"/>
    </svg>
    <div class="wordmark">Kelvaro<span class="wordmark__dot"></span></div>
    <div class="holder">
      <p class="holder__name">Tobias Vrenholt</p>
      <p class="holder__title">CEO</p>
    </div>
    <div class="divider"></div>
    <ul class="contacts">
      <li><svg viewBox="0 0 16 16" aria-label="Telephone"><path d="M2 5c0-2 3-3 6-3s6 1 6 3v1h-3V5H5v1H2z M4 7h8l2 6H2z"/></svg>+46 712 418257</li>
      <li><svg viewBox="0 0 16 16" aria-label="Mobile"><path d="M4 1h8v14H4z M5 3v9h6V3z"/></svg>+46 712 418257</li>
      <li><svg viewBox="0 0 16 16" aria-label="Email"><path d="M1 3h14v10H1z M2 4v1l6 4 6-4V4z"/></svg>tobias@kelvaro.se</li>
    </ul>
  </section>
</main>
</body>
</html>
```